Content processing platform needs a new front page design

We need a new front page design for Plumtext.com. Plumtext.com is a free content processing platform that helps online businesses and freelancers scale their production of content and translation. See pdf for a mockup on what we wish to communicate and layout of the front page. The final design should communicate scalability/growth and we hope to see a design where the user clicks one of the links for iGaming, e-shop, agency in the middle. 60% of our traffic is from mobile devices..

Number of Pages Required

1 page

Font styles to use
Other font styles liked:
• open sans

```html
<!DOCTYPE html>
<html lang="en">
<head>
<meta charset="utf-8">
<title>Plumtext – Scale your production of content and translation</title>
<link href="https://fonts.googleapis.com/css2?family=Open+Sans:wght@400;600;700&display=swap" rel="stylesheet">
<style>
:root{
  --blue:#1b8fd9;
  --blue-dark:#0f5d96;
  --pink:#e8175d;
  --ink:#222;
  --text:#555;
  --muted:#888;
  --line:#e3e3e3;
  --band:#2c2c2c;
  --footer:#161616;
  --footer-bar:#0c0c0c;
  --soft:#f4f4f4;
}
*{box-sizing:border-box;margin:0;padding:0}
html,body{width:1200px;height:4009px;overflow:hidden}
body{font-family:"Open Sans",Arial,sans-serif;color:var(--ink);background:#fff;position:relative}
a{color:inherit;text-decoration:none}
.abs{position:absolute}
section,header,footer{position:absolute;left:0;width:1200px}

/* header */
.site-header{top:0;height:100px;border-bottom:1px solid var(--line);background:#fff;z-index:3}
.brand{left:100px;top:28px;font-size:30px;font-weight:700;color:var(--blue);letter-spacing:-.5px}
.brand sup{font-size:11px;font-weight:600;background:var(--blue);color:#fff;padding:1px 4px;margin-left:3px;vertical-align:top;position:relative;top:8px}
.hdr-btn{top:28px;height:46px;border:1px solid var(--blue);color:var(--blue);font-size:14px;display:flex;align-items:center;justify-content:center;text-transform:uppercase}
.main-nav{top:100px;height:80px;z-index:3}
.main-nav a{position:absolute;top:28px;font-size:14px;font-weight:700;color:var(--ink)}
.caret{display:inline-block;width:0;height:0;border-left:4px solid transparent;border-right:4px solid transparent;border-top:5px solid var(--ink);margin-left:6px;vertical-align:middle}

/* hero */
.hero{top:100px;height:573px;background:linear-gradient(180deg,#fff 0%,#fff 65%,#ececec 100%);overflow:hidden}
.hero h1{left:100px;top:145px;width:580px;font-size:30px;line-height:1.55;font-weight:700}
.hero-col{top:285px;width:240px}
.hero-col h2{font-size:23px;font-weight:700;margin-bottom:14px}
.hero-col p{font-size:14px;line-height:1.8;color:var(--text)}
.hero-col .learn{display:inline-block;margin-top:4px;font-size:14px;color:var(--blue);text-decoration:underline}
.hero-divider{left:365px;top:285px;width:1px;height:165px;background:var(--line)}
.btn-pink{background:var(--pink);color:#fff}
.btn-pink-out{border:1px solid var(--pink);color:var(--pink);background:#fff}
.hero-btn{top:435px;height:46px;font-size:14px;display:flex;align-items:center;justify-content:center;text-transform:uppercase}

/* crowd band */
.crowd{top:673px;height:108px;background:var(--band);text-align:center;color:#fff}
.crowd h3{margin-top:25px;font-size:16px;font-weight:400;letter-spacing:.5px}
.crowd p{margin-top:12px;font-size:14px;color:var(--blue)}

.section-title{font-size:30px;font-weight:700;color:var(--pink);text-align:center;width:100%}

/* scale */
.scale{top:781px;height:369px}
.scale .section-title{top:75px}
.scale-item{top:180px;height:110px;text-align:center;font-size:19px;color:var(--ink)}
.scale-item svg{display:block;margin:0 auto 14px}
.scale-item + .scale-item{border-left:1px solid var(--line)}

/* partner strip */
.partners{top:1150px;height:106px;border-top:2px solid #5aaee4;border-bottom:2px solid #5aaee4;display:flex;align-items:center;justify-content:center;gap:34px;padding:0 110px}
.partner{font-size:25px;font-weight:600;color:#3a3a3a;display:flex;align-items:center;gap:6px;white-space:nowrap}
.partner i{display:inline-block;width:30px;height:30px;background:#3a3a3a}

/* why */
.why{top:1256px;height:530px}
.why .section-title{top:75px}
.why-col{top:185px;height:260px;text-align:center}
.why-col + .why-col{border-left:1px solid var(--line)}
.why-col svg{display:block;margin:0 auto}
.why-col h3{margin-top:20px;font-size:23px;font-weight:700}
.why-col p{margin:16px auto 0;width:270px;font-size:14px;line-height:1.9;color:var(--text)}

/* signup */
.signup{top:1786px;height:345px}
.signup svg.bg{position:absolute;left:0;top:0}
.signup h2{top:45px;width:100%;text-align:center;font-size:31px;font-weight:700;color:#fff}
.signup p{top:108px;width:100%;text-align:center;font-size:22px;color:#dbeefb}
.signup a{left:487px;top:168px;width:226px;height:45px;border:1px solid #fff;color:#fff;font-size:16px;display:flex;align-items:center;justify-content:center}

/* products */
.products{top:2131px;height:515px}
.device{left:430px;top:45px;width:675px;height:395px;border-radius:14px 14px 4px 4px;background:linear-gradient(180deg,#2a2a2a 0%,#1a1a1a 100%);padding:16px 18px 34px}
.device .screen{width:100%;height:100%;background:linear-gradient(180deg,#fafafa,#e8eef4)}
.device-base{left:415px;top:440px;width:705px;height:14px;border-radius:0 0 20px 20px;background:linear-gradient(180deg,#d6d6d6,#a9a9a9)}
.offer{left:100px;width:395px;padding:22px 20px 22px 70px;border:1px solid var(--line);background:#fff;z-index:2}
.offer svg{position:absolute;left:18px;top:20px}
.offer h4{font-size:14px;font-weight:700;color:var(--pink);text-transform:uppercase;margin-bottom:10px}
.offer p{font-size:14px;line-height:1.8;color:var(--text)}
.offer.active{background:var(--pink);border-color:var(--pink)}
.offer.active h4,.offer.active p{color:#fff}

/* word */
.word{top:2646px;height:420px;background:var(--soft)}
.word h2{left:100px;font-size:31px;font-weight:700;color:#2b2b2b}
.word p{left:100px;top:180px;width:1000px;font-size:14px;line-height:2.45;color:var(--text)}
.word .more{left:97px;top:300px;font-size:16px;font-weight:700;color:var(--blue)}

/* testimonial */
.quote{top:3000px;height:350px}
.quote svg.bg{position:absolute;left:0;top:0}
.quote h2{top:115px;width:100%;text-align:center;font-size:31px;font-weight:700;color:#fff;text-transform:uppercase}
.quote p{left:215px;top:185px;width:770px;text-align:center;font-size:14px;line-height:2.4;color:#fff}
.qmark{font-size:90px;font-weight:700;color:#3fa7ef;line-height:1}

/* users */
.users{top:3350px;height:230px}
.user{top:50px;height:110px;display:flex;align-items:center;gap:22px;padding-left:40px}
.user + .user{border-left:1px solid var(--line)}
.avatar{width:96px;height:96px;border-radius:50%;background:radial-gradient(circle at 50% 40%,#c9a587,#6e5a4a 70%)}
.avatar.on{border:5px solid var(--blue)}
.user h5{font-size:18px;font-weight:700;text-transform:uppercase}
.user span{display:block;margin-top:8px;font-size:14px;color:var(--text)}
.pointer{left:490px;top:36px;width:0;height:0;border-left:12px solid transparent;border-right:12px solid transparent;border-bottom:14px solid var(--blue)}

/* footer */
.site-footer{top:3500px;height:456px}
.site-footer svg.bg{position:absolute;left:0;top:0}
.f-col{top:210px}
.f-col h6{font-size:19px;font-weight:700;color:#fff;text-transform:uppercase;margin-bottom:22px}
.f-col a{display:block;font-size:13px;line-height:26.5px;color:var(--blue)}
.f-col li{list-style:none;display:flex;align-items:center;gap:14px;font-size:13px;color:#ddd;line-height:22px;margin-bottom:18px}
.f-div{top:210px;width:1px;height:210px;background:#333}
.lang{left:1007px;top:240px}
.lang b{display:block;font-size:19px;color:var(--blue);font-weight:700}
.lang span{display:block;margin-top:14px;font-size:11px;color:#ddd}
.bottom-bar{top:3956px;height:53px;background:var(--footer-bar)}
.social{left:113px;top:14px;display:flex;gap:12px}
.social i{display:block;width:26px;height:26px;border-radius:50%;background:#fff}
.copy{left:870px;top:17px;font-size:13px;color:#ddd}
.chat{left:1150px;top:3910px;width:36px;height:36px;border-radius:50%;background:var(--pink);display:flex;align-items:center;justify-content:center;z-index:5}
</style>
</head>
<body>

<header class="site-header">
  <a class="abs brand" href="#">Plumtext<sup>beta</sup></a>
  <a class="abs hdr-btn" style="left:600px;width:238px" href="#">Scale your business</a>
  <a class="abs hdr-btn" style="left:863px;width:237px" href="#">Become a freelancer</a>
</header>

<section class="hero">
  <div role="img" aria-label="Photo of hands typing on a laptop keyboard" class="abs" style="left:0;top:330px;width:1200px;height:243px;background:linear-gradient(180deg,rgba(255,255,255,0) 0%,#dcdcdc 60%,#cfcfcf 100%)"></div>
  <svg class="abs" style="left:0;top:0" width="1200" height="573" aria-hidden="true">
    <polygon points="640,160 1200,12 1200,520 1080,573 880,573" fill="var(--blue)"/>
  </svg>
  <div role="img" aria-label="Laptop showing the Plumtext dashboard" class="abs" style="left:690px;top:140px;width:470px;height:280px;border-radius:12px 12px 3px 3px;background:#1c1c1c;padding:12px 14px 26px">
    <div style="width:100%;height:100%;background:linear-gradient(90deg,#f3f3f3 0%,#fff 30%,#f6f6f6 100%)"></div>
  </div>
  <div class="abs" style="left:670px;top:420px;width:510px;height:12px;border-radius:0 0 16px 16px;background:linear-gradient(180deg,#ddd,#aaa)"></div>

  <h1 class="abs">Scale your production of content and translation with our free platform.</h1>
  <div class="abs hero-col" style="left:100px">
    <h2>Business</h2>
    <p>Scale your online content. Free<br>with your team or use our crowd.</p>
    <a class="learn" href="#">Learn more</a>
  </div>
  <div class="hero-divider abs"></div>
  <div class="abs hero-col" style="left:423px">
    <h2>Freelance</h2>
    <p>Freelance when you want.<br>Earn with your language skills.</p>
    <a class="learn" href="#">Learn more</a>
  </div>
  <a class="abs hero-btn btn-pink" style="left:100px;width:208px" href="#">Sign up to scale content</a>
  <a class="abs hero-btn btn-pink-out" style="left:423px;width:208px" href="#">Sign up to freelance</a>
</section>

<nav class="main-nav">
  <a href="#" style="left:273px">PRODUCTS<span class="caret"></span></a>
  <a href="#" style="left:428px">APPS<span class="caret"></span></a>
  <a href="#" style="left:540px">PRICES</a>
  <a href="#" style="left:656px">BLOG</a>
  <a href="#" style="left:762px">HELP</a>
  <a href="#" style="left:866px">CENTER</a>
</nav>

<section class="crowd">
  <h3>LATEST CONTENT FROM THE CROWD</h3>
  <p>Sander published the text shopnoord.example in Dutch 4 minutes ago.</p>
</section>

<section class="scale">
  <h2 class="abs section-title">What Do You Want to Scale?</h2>
  <a class="abs scale-item" href="#" style="left:100px;width:160px">
    <svg width="72" height="46" viewBox="0 0 72 46" fill="none" stroke="#222" stroke-width="3"><rect x="3" y="8" width="66" height="30" rx="15"/><path d="M18 17v12M12 23h12"/><circle cx="48" cy="20" r="3"/><circle cx="56" cy="26" r="3"/></svg>iGaming</a>
  <a class="abs scale-item" href="#" style="left:260px;width:165px">
    <svg width="56" height="56" viewBox="0 0 56 56" fill="none" stroke="#222" stroke-width="3"><path d="M6 22h44l-5 28H11z"/><path d="M16 22l8-16M40 22l-8-16"/><path d="M20 30v12M28 30v12M36 30v12"/></svg>eShop</a>
  <a class="abs scale-item" href="#" style="left:425px;width:220px">
    <svg width="56" height="56" viewBox="0 0 56 56" fill="none" stroke="#222" stroke-width="3"><circle cx="28" cy="28" r="22"/><circle cx="28" cy="28" r="12"/><path d="M28 2v14M28 40v14M2 28h14M40 28h14"/></svg>New Markets</a>
  <a class="abs scale-item" href="#" style="left:645px;width:175px">
    <svg width="56" height="56" viewBox="0 0 56 56" fill="none" stroke="#222" stroke-width="3"><rect x="8" y="8" width="40" height="32"/><circle cx="28" cy="24" r="8"/><path d="M20 48h16M28 40v8"/></svg>Agency</a>
  <a class="abs scale-item" href="#" style="left:820px;width:280px">
    <svg width="60" height="56" viewBox="0 0 60 56" fill="none" stroke="#222" stroke-width="3"><circle cx="22" cy="14" r="8"/><path d="M8 50V32c0-6 6-9 14-9s14 3 14 9v18"/><rect x="38" y="8" width="18" height="14"/><path d="M34 50h24"/></svg>Professional Freelancing</a>
</section>

<section class="partners" aria-label="Clients">
  <span class="partner">NORTHWARD RETAIL</span>
  <span class="partner"><i></i>Hallberg Group</span>
  <span class="partner">ClickWave</span>
  <span class="partner">Redfox</span>
  <span class="partner">PANTRYTIME</span>
  <span class="partner">Tundra</span>
</section>

<section class="why">
  <h2 class="abs section-title">Why Online Businesses Use Plumtext</h2>
  <div class="abs why-col" style="left:100px;width:320px">
    <svg width="80" height="80" viewBox="0 0 80 80"><rect x="14" y="6" width="40" height="54" rx="3" fill="none" stroke="var(--blue)" stroke-width="4"/><path d="M22 20h24M22 30h24M22 40h16" stroke="var(--blue)" stroke-width="4"/><circle cx="54" cy="56" r="16" fill="var(--blue)"/><path d="M54 50v2M54 56v8" stroke="#fff" stroke-width="4"/></svg>
    <h3>50% Cheaper</h3>
    <p>Online businesses using Plumtext save on average 50% on their internal and external costs for content and translation</p>
  </div>
  <div class="abs why-col" style="left:420px;width:370px">
    <svg width="80" height="80" viewBox="0 0 80 80" fill="none"><circle cx="44" cy="44" r="26" stroke="var(--blue)" stroke-width="4"/><path d="M44 44V28M44 44l10 8" stroke="var(--pink)" stroke-width="4"/><path d="M38 10h12M44 10v8" stroke="var(--blue)" stroke-width="4"/><path d="M4 38h12M8 48h8M4 58h12" stroke="var(--pink)" stroke-width="4"/></svg>
    <h3>10x Faster</h3>
    <p>With 1000s of Freelance writers and translators Plumtext saves you tons of time</p>
  </div>
  <div class="abs why-col" style="left:790px;width:310px">
    <svg width="80" height="80" viewBox="0 0 80 80"><circle cx="32" cy="32" r="18" fill="none" stroke="var(--blue)" stroke-width="10" stroke-dasharray="7 5"/><circle cx="32" cy="32" r="7" fill="var(--blue)"/><circle cx="56" cy="56" r="13" fill="none" stroke="var(--pink)" stroke-width="8" stroke-dasharray="6 4"/><circle cx="56" cy="56" r="5" fill="var(--pink)"/></svg>
    <h3>100% Automated</h3>
    <p>Plumtext features 100% automated workflows including Plagiarism Scan and uploading texts to your site</p>
  </div>
</section>

<section class="signup">
  <svg class="bg" width="1200" height="345" aria-hidden="true"><polygon points="0,0 1200,0 1200,259 0,340" fill="var(--blue)"/></svg>
  <h2 class="abs">Sign Up Now</h2>
  <p class="abs">for yourself, without charge</p>
  <a class="abs" href="#">Get Started - It's Free!</a>
</section>

<section class="products">
  <div class="abs device" role="img" aria-label="Laptop showing project statistics with a bar chart"><div class="screen"></div></div>
  <div class="abs device-base"></div>
  <div class="abs offer active" style="top:64px;height:108px">
    <svg width="34" height="30" viewBox="0 0 34 30" fill="none" stroke="#fff" stroke-width="2.5"><path d="M2 3h6l4 16h16l4-12H10"/><circle cx="14" cy="25" r="2.5"/><circle cx="26" cy="25" r="2.5"/></svg>
    <h4>Ecommerce Content</h4>
    <p>We have expert solutions for multilingual eShops with more than 2000 products</p>
  </div>
  <div class="abs offer" style="top:172px;height:110px">
    <svg width="36" height="26" viewBox="0 0 36 26" fill="none" stroke="var(--blue)" stroke-width="2.5"><rect x="2" y="4" width="32" height="18" rx="9"/><path d="M11 9v8M7 13h8"/><circle cx="25" cy="13" r="2"/></svg>
    <h4>iGaming Content</h4>
    <p>We provide content &amp; translations to the world's leading operators and affiliates</p>
  </div>
  <div class="abs offer" style="top:282px;height:130px">
    <svg width="36" height="34" viewBox="0 0 36 34" fill="none" stroke="var(--blue)" stroke-width="2.5"><circle cx="12" cy="12" r="8"/><circle cx="26" cy="22" r="8"/><circle cx="12" cy="12" r="3"/><circle cx="26" cy="22" r="3"/></svg>
    <h4>Self-Service Content &amp; Translations</h4>
    <p>Small and medium size websites can get up and running with our self-service products</p>
  </div>
</section>

<section class="word">
  <h2 class="abs" style="top:60px">Plum Text</h2>
  <h2 class="abs" style="top:110px">Why Plum Text, or even Plums Text for e-commerce?</h2>
  <p class="abs">You probably noticed that we wrote Plumtext in two words above. The reason obviously being that Plum Text, or Plums Text, has roughly 10 times more searches than just Plumtext. Well, on-page content is about generating traffic, and this is what we do. So, for the next 1500 words, and exclusively to this landing page, we will refer to ourselves as Plum Text.</p>
  <a class="abs more" href="#">Read more &nbsp;›</a>
</section>

<section class="quote">
  <svg class="bg" width="1200" height="350" aria-hidden="true"><polygon points="0,70 1200,0 1200,350 0,350" fill="var(--blue-dark)"/></svg>
  <div class="abs qmark" style="left:135px;top:160px">“</div>
  <h2 class="abs">What our users are saying</h2>
  <p class="abs">After days at sea, I really enjoy sitting in some coffeeshop, opening my computer and connecting with other Plumtext writers and work with words instead of ropes and sails. And more! With Plumtext, I have discovered some corners of the digital world that I would otherwise have never visited. So, even while working I keep traveling.</p>
  <div class="abs qmark" style="left:1010px;top:270px">”</div>
</section>

<section class="users">
  <div class="abs user" style="left:100px;width:325px">
    <div class="avatar" role="img" aria-label="Portrait photo of Tor"></div>
    <div><h5>Tor</h5><span>Freelance writer</span></div>
  </div>
  <div class="abs pointer"></div>
  <div class="abs user" style="left:425px;width:350px">
    <div class="avatar on" role="img" aria-label="Portrait photo of Paula"></div>
    <div><h5>Paula</h5><span>Freelance writer</span></div>
  </div>
  <div class="abs user" style="left:775px;width:325px">
    <div class="avatar" role="img" aria-label="Portrait photo of Vera" style="background:radial-gradient(circle at 50% 40%,#a7b4c2,#4d5e70 70%)"></div>
    <div><h5>Vera</h5><span>Freelance writer</span></div>
  </div>
</section>

<footer class="site-footer">
  <svg class="bg" width="1200" height="456" aria-hidden="true"><polygon points="0,180 1200,20 1200,456 0,456" fill="var(--footer)"/></svg>
  <div class="abs f-col" style="left:113px">
    <h6>Plumtext</h6>
    <a href="#">About Us</a><a href="#">Team</a><a href="#">Contact</a><a href="#">Terms of Service</a><a href="#">Privacy Policy</a><a href="#">Imprint</a>
  </div>
  <div class="abs f-div" style="left:325px"></div>
  <div class="abs f-col" style="left:370px">
    <h6>Resources</h6>
    <a href="#">Plumtext Affiliate</a><a href="#">Careers</a><a href="#">Developer Resources</a><a href="#">Plumtext Workshops</a><a href="#">Help</a>
  </div>
  <div class="abs f-div" style="left:580px"></div>
  <div class="abs f-col" style="left:650px">
    <h6>Contact</h6>
    <ul>
      <li><svg width="14" height="18" viewBox="0 0 14 18"><path d="M7 1a6 6 0 0 1 6 6c0 4-6 10-6 10S1 11 1 7a6 6 0 0 1 6-6z" fill="#ddd"/><circle cx="7" cy="7" r="2" fill="#161616"/></svg><span>Plumtext B.V., Havenkade 41<br>2811 AB Lindhaven, The Netherlands</span></li>
      <li><svg width="14" height="14" viewBox="0 0 14 14"><path d="M3 1l3 3-2 2c1 2 2 3 4 4l2-2 3 3-2 2C6 13 1 8 1 3z" fill="#ddd"/></svg><span>Tel: +31 (0)10 555 0192</span></li>
      <li><svg width="14" height="11" viewBox="0 0 14 11"><rect width="14" height="11" fill="#ddd"/><path d="M0 0l7 6 7-6" stroke="#161616" fill="none"/></svg><span>Email : hello@plumtext.com</span></li>
    </ul>
  </div>
  <div class="abs f-div" style="left:955px"></div>
  <div class="abs lang"><b>ENGLISH</b><span>TÜRKÇE</span></div>
</footer>

<div class="abs chat" aria-label="Chat"><svg width="16" height="16" viewBox="0 0 16 16"><rect x="1" y="1" width="14" height="11" rx="3" fill="#fff"/><path d="M4 12l-1 3 4-3" fill="#fff"/></svg></div>

<footer class="bottom-bar">
  <div class="abs social" aria-label="Social links"><i></i><i></i><i></i><i></i><i></i></div>
  <p class="abs copy">© 2018 Plumtext. All Rights Reserved.</p>
</footer>

</body>
</html>
```